Corporate Design für ein Installationsunternehmen
Wir sind mit dem Endergebnis sehr glücklich und zufrieden! Pelle ist auf alle unsere Wünsche und Vorschläge ohne zu zögern und mit viel Geduld eingegangen und wir können seine Arbeit wärmstens empfehlen. Vielen Dank nochmal Pelle für das tolle Design.
Zielgruppe
Wir sind ein Installationsunternehmen im Bereich Gas-, Wasser- und Heizung.
Aufgabenstellung
Das Symbol des Triskele sollte im Logo kreativ integriert werden ( wir sind jedoch offen auch für andere kreative Vorschläge die uns inspirieren).
Sauber, akkurat, symmetrisch und professionell soll es rüber kommen.
Das Symbol soll Vertrauen im Kunden wecken.

```html
<!DOCTYPE html>
<html lang="de">
<head>
<meta charset="utf-8">
<title>Zentara – Geschäftsausstattung</title>
<link href="https://fonts.googleapis.com/css2?family=Raleway:wght@400;500;700;800&display=swap" rel="stylesheet">
<style>
  :root {
    --bg: #e4e5e8;
    --paper: #ffffff;
    --navy: #0a1a33;
    --navy-deep: #06122a;
    --navy-flap: #0c1f3c;
    --window: #102748;
    --ink: #1d2433;
    --muted: #6b7180;
    --accent: #1f82dc;
    --kraft: #9c7a58;
    --string: #b89a7a;
  }
  * { box-sizing: border-box; margin: 0; padding: 0; }
  html, body { width: 1200px; height: 799px; overflow: hidden; }
  body {
    background: var(--bg);
    font-family: "Raleway", sans-serif;
    color: var(--ink);
    position: relative;
  }
  .sheet { position: absolute; overflow: hidden; box-shadow: 0 6px 18px rgba(0,0,0,.14); }
  .edge-rule { position: absolute; left: 0; bottom: 0; width: 100%; height: 4px; background: var(--accent); }

  .brand { display: flex; align-items: center; gap: 8px; }
  .brand-dot { width: 16px; height: 16px; border-radius: 50%; background: var(--accent); flex: none; }
  .brand-name { font-weight: 800; letter-spacing: .08em; text-transform: uppercase; font-size: 20px; color: var(--navy); }
  .on-dark .brand-name { color: #fff; }

  /* Letterhead */
  .letterhead { left: 60px; top: 32px; width: 520px; height: 735px; background: var(--paper); }
  .letterhead .brand { position: absolute; left: 52px; top: 50px; }
  .letter-body { position: absolute; left: 52px; top: 150px; width: 400px; font-size: 10.5px; line-height: 1.55; color: var(--ink); }
  .letter-body p { margin-bottom: 12px; }
  .signature { width: 110px; height: 30px; background: linear-gradient(90deg, #d9dbe0, #eef0f3); border-radius: 3px; margin-top: 6px; }
  .letter-footer { position: absolute; left: 52px; right: 40px; bottom: 56px; display: flex; justify-content: space-between; font-size: 7px; line-height: 1.6; color: var(--muted); text-transform: uppercase; letter-spacing: .03em; }

  /* Window envelope */
  .envelope-window { left: 640px; top: 32px; width: 500px; height: 250px; background: var(--navy); }
  .envelope-window .brand { position: absolute; left: 36px; top: 36px; }
  .address-window { position: absolute; right: 40px; bottom: 44px; width: 190px; height: 60px; background: var(--window); border-radius: 4px; }

  /* Business cards */
  .card-front { left: 640px; top: 310px; width: 240px; height: 150px; background: var(--paper); }
  .card-front .brand { position: absolute; left: 16px; top: 20px; gap: 6px; }
  .card-front .brand-name { font-size: 13px; }
  .card-front .brand-dot { width: 11px; height: 11px; }
  .card-person { position: absolute; right: 16px; top: 20px; text-align: right; }
  .card-person h2 { font-size: 13px; font-weight: 800; letter-spacing: .06em; color: var(--navy); }
  .card-person span { font-size: 7px; font-weight: 500; letter-spacing: .08em; color: var(--muted); }
  .card-contacts { position: absolute; right: 16px; top: 62px; list-style: none; font-size: 6.5px; color: var(--ink); }
  .card-contacts li { display: flex; justify-content: flex-end; align-items: center; gap: 5px; margin-bottom: 5px; }
  .card-contacts svg { width: 7px; height: 7px; fill: var(--navy); }

  .card-back { left: 900px; top: 310px; width: 240px; height: 150px; background: var(--navy-deep); display: flex; align-items: center; justify-content: center; }
  .card-back .brand-name { font-size: 15px; }
  .card-back .brand-dot { width: 12px; height: 12px; }

  /* Button envelope */
  .envelope-button { left: 640px; top: 488px; width: 500px; height: 279px; background: var(--navy); }
  .envelope-flap { position: absolute; left: 0; top: 0; width: 170px; height: 279px; border-right: 1px solid rgba(255,255,255,.08); background: var(--navy-flap); }
  .button-tie { position: absolute; width: 20px; height: 20px; border-radius: 50%; background: var(--kraft); }
  .tie-string { position: absolute; left: 0; top: 0; }
  .envelope-button .brand { position: absolute; right: 40px; bottom: 40px; }
</style>
</head>
<body>

  <section class="sheet letterhead">
    <div class="brand"><span class="brand-dot"></span><span class="brand-name">Zentara</span></div>
    <div class="letter-body">
      <p>Sehr geehrte Damen und Herren,</p>
      <p>Zentara Gas Wasser Heizung – wir planen, installieren und warten Ihre Haustechnik zuverlässig und termingerecht.</p>
      <p>Als Installationsunternehmen im Bereich Gas-, Wasser- und Heizung stehen wir für saubere, akkurate und professionelle Arbeit. Unser Team berät Sie gern persönlich und findet für jedes Vorhaben eine passende Lösung, vom Neubau bis zur Sanierung.</p>
      <p>Zentara Gas Wasser Heizung – Vertrauen, das man spürt. Wir freuen uns auf Ihre Anfrage.</p>
      <p>Mit freundlichen Grüßen</p>
      <div class="signature" role="img" aria-label="Handschriftliche Unterschrift"></div>
    </div>
    <div class="letter-footer">
      <div>Zentara Haustechnik GmbH<br>Geschäftsführer: Lena Brandt<br>Prokurist: Jonas Weber</div>
      <div>Lindenweg 12<br>01234 Musterstadt<br>Tel. 030 5550 1789<br>www.zentara.de</div>
      <div>Bankverbindung<br>Musterbank eG<br>IBAN DE00 1234 5678 90<br>BIC MUSTDEXX</div>
    </div>
    <div class="edge-rule"></div>
  </section>

  <section class="sheet envelope-window on-dark">
    <div class="brand"><span class="brand-dot"></span><span class="brand-name">Zentara</span></div>
    <div class="address-window"></div>
    <div class="edge-rule"></div>
  </section>

  <section class="sheet card-front">
    <div class="brand"><span class="brand-dot"></span><span class="brand-name">Zentara</span></div>
    <div class="card-person">
      <h2>JOHN DOE</h2>
      <span>SENIOR CONSULTANT</span>
    </div>
    <ul class="card-contacts">
      <li>+49 30 5550 1789 <svg viewBox="0 0 10 10"><path d="M2 0h2l1 3-1.5 1a6 6 0 0 0 2.5 2.5L7 5l3 1v2a2 2 0 0 1-2 2A8 8 0 0 1 0 2a2 2 0 0 1 2-2z"/></svg></li>
      <li>john.doe@zentara.de <svg viewBox="0 0 10 10"><path d="M0 2h10v6H0z M0 2l5 3.5L10 2"/></svg></li>
      <li>Lindenweg 12, Musterstadt <svg viewBox="0 0 10 10"><path d="M5 0a3.5 3.5 0 0 1 3.5 3.5C8.5 6 5 10 5 10S1.5 6 1.5 3.5A3.5 3.5 0 0 1 5 0zm0 2a1.5 1.5 0 1 0 0 3 1.5 1.5 0 0 0 0-3z"/></svg></li>
    </ul>
    <div class="edge-rule"></div>
  </section>

  <section class="sheet card-back on-dark">
    <div class="brand"><span class="brand-dot"></span><span class="brand-name">Zentara</span></div>
  </section>

  <section class="sheet envelope-button on-dark">
    <div class="envelope-flap"></div>
    <svg class="tie-string" width="500" height="279" aria-hidden="true">
      <path d="M70 70 Q110 120 140 160" stroke="var(--string)" stroke-width="1" fill="none"/>
    </svg>
    <span class="button-tie" style="left:60px; top:60px;"></span>
    <span class="button-tie" style="left:130px; top:150px;"></span>
    <div class="brand"><span class="brand-dot"></span><span class="brand-name">Zentara</span></div>
  </section>

</body>
</html>
```